Verindo Living- Hang tags for Modern Handmade Home Decor products

We need to design some hang tags to use for our products, we want double tags, meaning two tags that go together on one string, two different and coordinating sizes and shapes. We have a logo, what we need is the artwork for these two tags to take to print. One tag will have the logo on one side and company information on the other, the second tag will be for product information. For example, we specialize in handmade pieces from Latin America, on the product tag I want space to write the product info but also a line for what country it's from and what community created it. I'm attaching an image of the shapes of tags that I like, along with a copy of our logo. On the larger company tag I'd like our logo in the center and a color block stripe of the yellow color of our logo at the bottom, on the flip side there will just be text, sort of our company motto. On the narrower longer product info tag I'd like a small logo at the bottom end and space for product information to be written in by hand and on the flip side of this one lines for what country it's from, what community created it and care instructions, again, all information that we will write in by hand. Please let me know if you have questions.

Target Market(s)

Design savvy, house proud, well educated people who travel and appreciate art.

Font styles to use
Sans Serif

Requirements
Must have
• I want it to look graphic, sophisticated and modern. I want to be very legible and clean.
Nice to have
• Clarity, easy to read, and maybe a bit of whimsy or lightheartedness.
Should not have
• Nothing that feels "ethnic" or "crafty:, even though our products are handmade in Latin America they are contemporary and sophisticated, not stereotypical.

```html
<!DOCTYPE html>
<html lang="en">
<head>
<meta charset="utf-8">
<title>Verindo Living – Hang Tags</title>
<link rel="stylesheet" href="https://fonts.googleapis.com/css2?family=Questrial&family=Arimo:wght@400&display=swap">
<style>
  :root {
    --stage-edge: #777777;
    --stage-centre: #dcdcdc;
    --card-white: #ffffff;
    --card-mist: #d7dde2;
    --outline: #333333;
    --tab-black: #231f20;
    --brand-yellow: #f9cf0a;
    --brand-grey: #a9b5bd;
    --slogan-grey: #858585;
    --string: #a39d7c;
    --band-grey: #bdbdbd;
    --chip-grey: #d9dde0;
    --rule-grey: #9a9a9a;
    --ink: #222222;
  }
  * { box-sizing: border-box; margin: 0; padding: 0; }
  html, body { width: 1200px; height: 700px; overflow: hidden; }
  body {
    background: radial-gradient(ellipse 520px 420px at 600px 350px, var(--stage-centre), var(--stage-edge));
    font-family: "Questrial", "Century Gothic", sans-serif;
  }
  .stage { position: relative; width: 1200px; height: 700px; }

  .tag { position: absolute; }
  .tag-shape { position: absolute; inset: 0; overflow: visible; }
  .tag-content { position: absolute; inset: 0; }

  .tag--slogan   { left: 38px;  top: 115px; width: 317px; height: 434px; }
  .tag--logo     { left: 374px; top: 118px; width: 311px; height: 428px; }
  .tag--product  { left: 732px; top: 111px; width: 201px; height: 536px; }
  .tag--origin   { left: 948px; top: 117px; width: 200px; height: 528px; }

  .colour-stripe {
    position: absolute; left: 0; right: 0; bottom: 0;
    background: var(--brand-yellow);
  }
  .tag--slogan .colour-stripe { height: 37px; border: 1px solid var(--outline); border-top: 0; }
  .tag--logo .colour-stripe { height: 37px; border: 1px solid var(--outline); border-top: 0; }

  .slogan {
    position: absolute; left: 0; right: 0; top: 195px;
    text-align: center; font-style: italic;
    font-size: 27px; color: var(--slogan-grey); letter-spacing: 0.5px;
  }

  .brand { position: absolute; left: 0; right: 0; text-align: center; }
  .brand-dot { display: block; margin: 0 auto; border-radius: 50%; background: var(--brand-yellow); }
  .brand-name { display: block; color: var(--brand-grey); white-space: nowrap; }
  .brand-web { display: block; color: var(--brand-grey); white-space: nowrap; }

  .tag--slogan .brand { top: 290px; }
  .tag--slogan .brand-dot { width: 36px; height: 36px; }
  .tag--slogan .brand-name { font-size: 21px; margin-top: 14px; }
  .tag--slogan .brand-web { font-size: 6.5px; letter-spacing: 2px; margin-top: 4px; }

  .tag--logo .brand { top: 130px; }
  .tag--logo .brand-dot { width: 96px; height: 96px; }
  .tag--logo .brand-name { font-size: 38px; margin-top: 34px; letter-spacing: 1px; }
  .tag--logo .brand-web { font-size: 9.5px; letter-spacing: 3.2px; margin-top: 6px; }

  .product-heading {
    position: absolute; left: 0; right: 0; top: 104px; height: 32px;
    background: var(--band-grey); border: 1px dashed #8a8a8a;
    font-family: "Arimo", Arial, sans-serif; font-size: 14px; color: var(--ink);
    display: flex; align-items: center; justify-content: center; letter-spacing: 0.2px;
  }
  .product-heading::before, .product-heading::after {
    content: ""; position: absolute; left: 14px; right: 14px; height: 1px; background: var(--card-white);
  }
  .product-heading::before { top: 4px; }
  .product-heading::after { bottom: 4px; }

  .write-in-box {
    position: absolute; left: 14px; top: 156px; width: 174px; height: 203px;
    background: var(--card-white); border: 1px dotted #e6d37a;
    border-radius: 0 16px 0 16px;
  }
  .write-in-line {
    position: absolute; left: 11px; right: 9px; height: 0;
    border-top: 1px dotted var(--rule-grey);
  }

  .logo-panel {
    position: absolute; left: 0; right: 0; top: 403px; height: 119px;
    background: var(--card-white);
  }
  .tag--product .brand { top: 22px; }
  .tag--product .brand-dot { width: 32px; height: 32px; }
  .tag--product .brand-name { font-size: 18px; margin-top: 12px; }
  .tag--product .brand-web { font-size: 6px; letter-spacing: 1.6px; margin-top: 3px; }

  .origin-table {
    position: absolute; left: 16px; top: 151px; width: 166px; height: 252px;
    background: var(--card-white); border: 1px solid var(--ink);
    display: grid; grid-template-rows: 49px 45px 1fr;
  }
  .origin-row { border-bottom: 1px solid var(--ink); padding: 4px 0 0 3px; }
  .origin-row:last-child { border-bottom: 0; }
  .origin-label {
    display: inline-block; background: var(--chip-grey);
    font-family: "Arimo", Arial, sans-serif; font-size: 9.5px; color: var(--ink);
    padding: 2px 5px 2px 2px;
  }
  .origin-stripe {
    position: absolute; left: 16px; top: 406px; width: 166px; height: 9px;
    background: var(--brand-yellow);
  }
</style>
</head>
<body>
<main class="stage">

  <!-- Company tag, reverse: motto side -->
  <section class="tag tag--slogan">
    <svg class="tag-shape" width="317" height="434" viewBox="0 0 317 434" aria-hidden="true">
      <polygon points="0.5,47 47,0.5 270,0.5 316.5,47 316.5,433.5 0.5,433.5" fill="var(--card-white)" stroke="var(--outline)" stroke-width="1"/>
      <rect x="133" y="0" width="52" height="65" fill="var(--tab-black)"/>
      <circle cx="159" cy="33" r="8" fill="var(--card-white)"/>
      <path d="M159,33 C168,-20 200,-85 213,-88 C226,-92 214,-55 163,24" fill="none" stroke="var(--string)" stroke-width="3" stroke-linecap="round"/>
    </svg>
    <div class="tag-content">
      <p class="slogan">“slogan here”</p>
      <div class="brand">
        <span class="brand-dot"></span>
        <span class="brand-name">Verindo Living</span>
        <span class="brand-web">www.verindoliving.com</span>
      </div>
      <div class="colour-stripe"></div>
    </div>
  </section>

  <!-- Company tag, front: logo side -->
  <section class="tag tag--logo">
    <svg class="tag-shape" width="311" height="428" viewBox="0 0 311 428" aria-hidden="true">
      <polygon points="0.5,47 47,0.5 264,0.5 310.5,47 310.5,427.5 0.5,427.5" fill="var(--card-white)" stroke="var(--outline)" stroke-width="1"/>
      <rect x="130" y="0" width="51" height="64" fill="var(--tab-black)"/>
      <circle cx="155" cy="33" r="8" fill="var(--card-white)"/>
      <path d="M155,33 C166,-20 198,-85 212,-88 C225,-92 212,-55 159,24" fill="none" stroke="var(--string)" stroke-width="3" stroke-linecap="round"/>
    </svg>
    <div class="tag-content">
      <div class="brand">
        <span class="brand-dot"></span>
        <span class="brand-name">Verindo Living</span>
        <span class="brand-web">www.verindoliving.com</span>
      </div>
      <div class="colour-stripe"></div>
    </div>
  </section>

  <!-- Product tag, front: write-in product info -->
  <section class="tag tag--product">
    <svg class="tag-shape" width="201" height="536" viewBox="0 0 201 536" aria-hidden="true">
      <polygon points="0,45 42,0 159,0 201,45 201,536 0,536" fill="var(--card-mist)"/>
      <rect x="76" y="0" width="51" height="63" fill="var(--tab-black)"/>
      <circle cx="101" cy="31" r="8" fill="var(--card-white)"/>
      <path d="M101,31 C112,-20 140,-80 152,-84 C164,-88 154,-55 105,22" fill="none" stroke="var(--string)" stroke-width="3" stroke-linecap="round"/>
    </svg>
    <div class="tag-content">
      <h2 class="product-heading">PRODUCT INFO</h2>
      <div class="write-in-box">
        <span class="write-in-line" style="top:26px"></span>
        <span class="write-in-line" style="top:64px"></span>
        <span class="write-in-line" style="top:102px"></span>
        <span class="write-in-line" style="top:139px"></span>
        <span class="write-in-line" style="top:178px"></span>
      </div>
      <div class="logo-panel">
        <div class="brand">
          <span class="brand-dot"></span>
          <span class="brand-name">Verindo Living</span>
          <span class="brand-web">www.verindoliving.com</span>
        </div>
      </div>
    </div>
  </section>

  <!-- Product tag, reverse: origin and care -->
  <section class="tag tag--origin">
    <svg class="tag-shape" width="200" height="528" viewBox="0 0 200 528" aria-hidden="true">
      <polygon points="0,45 42,0 158,0 200,45 200,528 0,528" fill="var(--card-mist)"/>
      <rect x="76" y="0" width="50" height="61" fill="var(--tab-black)"/>
      <circle cx="101" cy="30" r="8" fill="var(--card-white)"/>
      <path d="M101,30 C112,-20 140,-82 152,-86 C164,-90 154,-55 105,21" fill="none" stroke="var(--string)" stroke-width="3" stroke-linecap="round"/>
    </svg>
    <div class="tag-content">
      <div class="origin-table">
        <div class="origin-row"><span class="origin-label">COUNTRY</span></div>
        <div class="origin-row"><span class="origin-label">COMMUNITY</span></div>
        <div class="origin-row"><span class="origin-label">CARE INFORMATION</span></div>
      </div>
      <div class="origin-stripe"></div>
    </div>
  </section>

</main>
</body>
</html>
```